Semi-anonymous photo sharing and messaging app

Design app interface. App is needed for semi-anonymous communication.

For instance if you are on a tour bus, and you just met some people there. You want to send them pictures, but you don't want to give your chatterly / email / phone number. So instead you use this app - current name is "eLumvo" but you can also suggest a name if it fits really well with the theme of the design.

The initial version of the app is in the tivora store
https://shop.tivora-apps.example/item?id=net.k7mzpwq2rt84vbnhsy3lc

the web version of this app is located here
https://plumtidelanternharbor.example/

it is called Plum Tide Lantern Harbor, because the password is four common words, and if you know those words, you can open the chat room.

As you can see app looks very poorly, and needs to be designed from bottom up. App should look nothing like it looks now. it should have original and easily recognizable feel to it.

I'm attaching screen-shots of the current app. Two screens - you enter password on one screen (or choose one of the existing "rooms") - you chat with peers on the second screen

It should be something neutral, so it's mainly for travellers, but could be used by anyone else. It should have vibe of comfort and security, but at the same time adventure and fun.

Please come back with more questions!

Target Market(s)

Travellers, mostly
single, groups,

Industry/Entity Type

Communication

Font styles to use
Sans Serif

Requirements
Must have
• original, light feel
• recognizable
• unique

```html
<!DOCTYPE html>
<html lang="en">
<head>
<meta charset="utf-8">
<title>Wordnest – App Interface Screens</title>
<link href="https://fonts.googleapis.com/css2?family=Roboto:wght@300;400;500;700&display=swap" rel="stylesheet">
<style>
:root{
  --canvas:#5cb6ef;
  --brand-blue:#1a93e3;
  --brand-blue-dark:#0d78c9;
  --tab-blue:#1e8fdf;
  --orange:#f07a1c;
  --white:#ffffff;
  --ink:#2b2b2b;
  --muted:#7a7a7a;
  --line:#d9d9d9;
  --green:#3a9a1e;
  --drawer-top:#3d4d68;
  --drawer-bottom:#17191d;
  --badge:#4a90e2;
  --photo-a:#8a9b6e;
  --photo-b:#6f8fa8;
  --photo-c:#b28a6e;
  --photo-d:#c9b48a;
  --photo-e:#5d7fa6;
  --photo-f:#a9794f;
}
*{box-sizing:border-box;margin:0;padding:0}
html,body{width:1200px;height:1000px;overflow:hidden}
body{background:var(--canvas);font-family:'Roboto',Arial,sans-serif;color:var(--ink);position:relative}
.icons{position:absolute;width:0;height:0}
.screen{position:absolute;width:273px;height:482px;overflow:hidden;background:#f2f2f2}
.row-1{top:16px}.row-2{top:512px}
.col-1{left:30px}.col-2{left:322px}.col-3{left:616px}.col-4{left:908px}
.abs{position:absolute}

/* splash + login */
.blue-bg{background:radial-gradient(circle at 50% 45%,#35b2f5 0%,var(--brand-blue) 45%,var(--brand-blue-dark) 100%)}
.brand-mark{position:absolute;border-radius:50%;background:var(--white);display:flex;align-items:center;justify-content:center;box-shadow:0 4px 10px rgba(0,0,0,.25)}
.brand-name{color:var(--orange);font-weight:700}
.spinner{left:120px;top:331px;width:32px;height:32px}
.tagline{color:var(--white);font-size:6.5px;text-align:center;line-height:1.35;left:30px;width:213px}
.copyright{color:var(--white);font-size:9.2px;text-align:center;left:0;width:273px;top:402px}
.rights{color:var(--white);font-size:12px;text-align:center;left:0;width:273px;top:422px}
.field{left:32px;width:214px;border-bottom:1px solid rgba(255,255,255,.8);height:22px;color:var(--white);font-size:12px;display:flex;align-items:center;gap:8px;padding-left:2px}
.field svg{width:14px;height:14px}
.login-btn{left:73px;top:276px;width:118px;height:26px;border:1.5px solid var(--white);color:var(--white);font-size:15px;display:flex;align-items:center;justify-content:center}
.create{left:0;width:273px;top:314px;text-align:center;color:var(--white);font-size:13px}
.divider{left:8px;width:258px;top:396px;border-top:1px solid rgba(255,255,255,.7)}
.social{top:419px;width:48px;height:48px;border:1.5px solid var(--white);border-radius:50%;color:var(--white);font-size:8px;display:flex;align-items:center;justify-content:center}

/* app chrome */
.status{left:0;top:0;width:273px;height:20px;font-size:10px;display:flex;align-items:center;justify-content:space-between;padding:0 6px;z-index:3}
.status .carrier{display:flex;align-items:center;gap:3px}
.status .time{font-weight:500}
.status.light{color:var(--white)}
.appbar{left:0;top:20px;width:273px;height:30px;display:flex;align-items:center;justify-content:space-between;padding:0 12px;z-index:3}
.appbar .title{font-size:12.5px;font-weight:500}
.appbar svg{width:22px;height:20px}
.collage{left:0;top:0;width:273px;height:443px;background:linear-gradient(160deg,#f4f1ee 0%,#eae6e2 40%,#f3f3f1 100%)}
.avatar{border-radius:50%;background:linear-gradient(180deg,#7f9a5c 0%,#6a7d52 45%,#1f3a68 100%);border:3px solid var(--white);box-shadow:0 1px 3px rgba(0,0,0,.25)}
.tabbar{left:0;top:443px;width:273px;height:39px;background:var(--tab-blue);display:flex;z-index:3}
.tab{flex:1;display:flex;flex-direction:column;align-items:center;justify-content:center;gap:2px;color:var(--white);font-size:5.2px;border-right:1px solid rgba(255,255,255,.25)}
.tab:last-child{border-right:0}
.tab svg{width:20px;height:20px}

/* four words */
.welcome{left:0;width:273px;text-align:center;font-size:10.5px;font-weight:500}
.words-box{left:10px;top:172px;width:252px;height:34px;background:var(--white);border:1px solid var(--line);display:flex;align-items:center}
.word{flex:1;text-align:center;color:var(--green);font-weight:700;font-size:12px;border-right:1px solid var(--line)}
.word:last-child{border-right:0}
.btn-blue{background:var(--tab-blue);color:var(--white);font-weight:500;font-size:12px;display:flex;align-items:center;justify-content:center;box-shadow:0 2px 3px rgba(0,0,0,.2)}
.recent-title{left:26px;top:324px;font-size:12px;font-weight:500}
.recent-item{left:26px;width:226px;font-size:9.5px;color:#555;display:flex;justify-content:space-between}

/* profile */
.cover{left:0;top:0;width:273px;height:178px;background:linear-gradient(135deg,#6b5a45 0%,#7a8a5a 35%,#a57a5a 65%,#4d5f78 100%)}
.profile-panel{left:0;top:178px;width:273px;height:265px;background:var(--white)}
.stat{font-size:9px;font-weight:700;text-align:center;line-height:1}
.stat small{display:block;font-size:6px;font-weight:400;color:var(--muted);margin-top:1px}
.grid{display:grid;gap:6px}
.photo{border:2px solid var(--white);box-shadow:0 0 0 1px #ddd}

/* drawer */
.drawer{left:0;top:0;width:228px;height:482px;background:linear-gradient(180deg,var(--drawer-top) 0%,#2a3140 50%,var(--drawer-bottom) 100%)}
.drawer-peek{left:228px;top:0;width:45px;height:482px;background:#eef0f2}
.menu-item{left:20px;width:208px;height:38px;color:var(--white);font-size:14px;font-weight:300;display:flex;align-items:center;gap:6px;border-bottom:1px solid rgba(255,255,255,.25)}
.menu-item svg{width:24px;height:24px}
.badge{width:14px;height:14px;border-radius:50%;background:var(--badge);color:var(--white);font-size:8px;display:flex;align-items:center;justify-content:center}
.history-bar{left:0;top:342px;width:228px;height:28px;background:rgba(0,0,0,.35);color:var(--white);display:flex;align-items:center;padding:0 16px;font-size:12px;font-weight:300}
.history-item{left:20px;width:190px;color:var(--white);display:flex;gap:6px}
.history-item .big{font-size:15px;font-weight:300;line-height:1}
.history-item .sub{font-size:8px;color:#c8c8c8}

/* chat */
.chat-bg{left:0;top:0;width:273px;height:443px;background:linear-gradient(170deg,#f6f4f1 0%,#efece8 50%,#f5f5f4 100%)}
.bubble{background:var(--white);border:1px solid #dcdcdc;border-radius:4px;box-shadow:0 1px 2px rgba(0,0,0,.12);padding:3px 6px}
.bubble-head{display:flex;justify-content:space-between;font-size:5.5px;color:#444;border-bottom:1px solid #e5e5e5;padding-bottom:2px;margin-bottom:4px}
.bubble-text{font-size:6.6px;color:#777;line-height:1.55}
.chat-avatar{width:36px;height:36px;border-width:2px}
.media{background:linear-gradient(180deg,#6f8f4c 0%,#5a7444 55%,#23406f 100%)}
.composer{left:0;top:443px;width:273px;height:39px;background:var(--tab-blue);z-index:3}
.composer .input{position:absolute;left:12px;top:7px;width:197px;height:25px;background:var(--white);border-radius:2px}
.composer .plus{position:absolute;left:12px;top:7px;width:25px;height:25px;background:#e3e3e3;color:#999;font-size:14px;display:flex;align-items:center;justify-content:center}
.composer .send{position:absolute;left:215px;top:6px;width:51px;height:26px;border:1px solid rgba(255,255,255,.6);border-radius:2px;color:var(--white);font-size:12px;font-weight:500;display:flex;align-items:center;justify-content:center;background:var(--brand-blue)}
.attach-panel{left:0;top:388px;width:273px;height:55px;background:#262626;color:var(--white);z-index:3}
.dim{left:0;top:0;width:273px;height:482px;background:rgba(0,0,0,.72);z-index:4}
.modal{left:12px;top:58px;width:247px;height:369px;background:#f3f3f3;border-radius:4px;z-index:5;overflow:hidden}
.modal-head{height:32px;background:linear-gradient(180deg,#fdfdfd,#e9e9e9);display:flex;align-items:center;justify-content:center;font-size:10px;border-bottom:1px solid #d3d3d3;position:relative}
.close{position:absolute;right:9px;top:7px;width:18px;height:18px;border:1px solid #888;border-radius:50%;font-size:10px;color:#555;display:flex;align-items:center;justify-content:center}
</style>
</head>
<body>

<svg class="icons" aria-hidden="true">
  <defs>
    <symbol id="i-gear" viewBox="0 0 24 24"><circle cx="12" cy="12" r="8" fill="none" stroke="currentColor" stroke-width="3" stroke-dasharray="3 2.3"/><circle cx="12" cy="12" r="6" fill="none" stroke="currentColor" stroke-width="1.4"/><circle cx="12" cy="12" r="2.5" fill="none" stroke="currentColor" stroke-width="1.4"/></symbol>
    <symbol id="i-mail" viewBox="0 0 24 22"><rect x="1" y="6" width="18" height="13" fill="none" stroke="currentColor" stroke-width="1.5"/><path d="M1 6l9 7 9-7" fill="none" stroke="currentColor" stroke-width="1.5"/><circle cx="19" cy="5" r="4" fill="#fff" stroke="currentColor" stroke-width="1"/><text x="19" y="7" font-size="5.5" text-anchor="middle" fill="currentColor" font-family="Roboto,sans-serif">2</text></symbol>
    <symbol id="i-bubble" viewBox="0 0 24 24"><path d="M4 4h16v12H10l-5 4v-4H4z" fill="none" stroke="currentColor" stroke-width="1.5"/><path d="M7 8h10M7 11h10" stroke="currentColor" stroke-width="1.2"/></symbol>
    <symbol id="i-person" viewBox="0 0 24 24"><circle cx="12" cy="8" r="4.5" fill="none" stroke="currentColor" stroke-width="1.5"/><path d="M3 22c0-5 4-8 9-8s9 3 9 8z" fill="none" stroke="currentColor" stroke-width="1.5"/></symbol>
    <symbol id="i-info" viewBox="0 0 24 24"><circle cx="12" cy="12" r="10" fill="none" stroke="currentColor" stroke-width="1.5"/><path d="M12 10v7" stroke="currentColor" stroke-width="1.8"/><circle cx="12" cy="7" r="1.2" fill="currentColor"/></symbol>
    <symbol id="i-four" viewBox="0 0 24 24"><circle cx="12" cy="12" r="10" fill="none" stroke="currentColor" stroke-width="1.5"/><text x="12" y="13" font-size="9" text-anchor="middle" fill="currentColor" font-family="Roboto,sans-serif">4</text><path d="M7 17h10" stroke="currentColor" stroke-width="1.2" stroke-dasharray="1 1.5"/></symbol>
    <symbol id="i-chats" viewBox="0 0 24 24"><path d="M3 5h13v9H8l-4 3v-3H3z" fill="none" stroke="currentColor" stroke-width="1.4"/><path d="M9 16v2h8l3 3v-3h1V9h-3" fill="none" stroke="currentColor" stroke-width="1.4"/></symbol>
    <symbol id="i-help" viewBox="0 0 24 24"><circle cx="12" cy="12" r="10" fill="none" stroke="currentColor" stroke-width="1.3"/><path d="M9 9.5a3 3 0 1 1 4 2.8c-.8.4-1 1-1 2" fill="none" stroke="currentColor" stroke-width="1.4"/><circle cx="12" cy="17" r="1" fill="currentColor"/></symbol>
    <symbol id="i-terms" viewBox="0 0 24 24"><rect x="2" y="5" width="20" height="14" fill="none" stroke="currentColor" stroke-width="1.3"/><rect x="5" y="8" width="5" height="4" fill="none" stroke="currentColor" stroke-width="1.1"/><path d="M12 9h7M12 12h7M5 15h14" stroke="currentColor" stroke-width="1.1"/></symbol>
    <symbol id="i-power" viewBox="0 0 24 24"><path d="M7.5 6.5a8 8 0 1 0 9 0" fill="none" stroke="currentColor" stroke-width="1.5"/><path d="M12 2v9" stroke="currentColor" stroke-width="1.5"/></symbol>
    <symbol id="i-aboutc" viewBox="0 0 24 24"><circle cx="12" cy="12" r="10" fill="none" stroke="currentColor" stroke-width="1.3"/><path d="M12 10v7" stroke="currentColor" stroke-width="1.6"/><circle cx="12" cy="7" r="1" fill="currentColor"/></symbol>
    <symbol id="i-user" viewBox="0 0 16 16"><circle cx="8" cy="5" r="3.2" fill="currentColor"/><path d="M1.5 15c0-4 3-6 6.5-6s6.5 2 6.5 6z" fill="currentColor"/></symbol>
    <symbol id="i-lock" viewBox="0 0 16 16"><rect x="2.5" y="7" width="11" height="8.5" fill="currentColor"/><path d="M5 7V4.5a3 3 0 0 1 6 0V7" fill="none" stroke="currentColor" stroke-width="1.5"/></symbol>
    <symbol id="i-wifi" viewBox="0 0 16 12"><path d="M1 4a10 10 0 0 1 14 0M3.5 6.5a6.5 6.5 0 0 1 9 0M6 9a3 3 0 0 1 4 0" fill="none" stroke="currentColor" stroke-width="1.4"/><circle cx="8" cy="11" r="1" fill="currentColor"/></symbol>
    <symbol id="i-battery" viewBox="0 0 24 12"><rect x="1" y="1" width="19" height="10" rx="2" fill="none" stroke="currentColor" stroke-width="1.2"/><rect x="2.5" y="2.5" width="16" height="7" fill="currentColor"/><rect x="21" y="4" width="2" height="4" fill="currentColor"/></symbol>
    <symbol id="i-bt" viewBox="0 0 10 14"><path d="M2 4l6 6-3 3V1l3 3-6 6" fill="none" stroke="currentColor" stroke-width="1.2"/></symbol>
    <symbol id="i-chev" viewBox="0 0 12 20"><path d="M2 2l8 8-8 8" fill="none" stroke="currentColor" stroke-width="1.6"/></symbol>
    <symbol id="i-cloud" viewBox="0 0 16 12"><path d="M4 11a3 3 0 0 1 0-6 4 4 0 0 1 8 0 3 3 0 0 1 0 6z" fill="#fff"/><path d="M8 5v4M6.5 7.5L8 9l1.5-1.5" fill="none" stroke="#333" stroke-width="1"/></symbol>
    <symbol id="i-picture" viewBox="0 0 36 28"><rect x="1" y="1" width="34" height="26" fill="none" stroke="currentColor" stroke-width="2"/><path d="M3 24l10-11 7 8 5-5 8 8z" fill="currentColor"/><circle cx="26" cy="8" r="3" fill="currentColor"/></symbol>
    <symbol id="i-play" viewBox="0 0 32 32"><circle cx="16" cy="16" r="15" fill="currentColor"/><path d="M12 9l11 7-11 7z" fill="#262626"/></symbol>
  </defs>
</svg>

<!-- ROW 1 · splash -->
<section class="screen row-1 col-1 blue-bg" aria-label="Splash screen">
  <div class="brand-mark" style="left:60px;top:142px;width:154px;height:154px">
    <span class="brand-name" style="font-size:24px">Wordnest</span>
  </div>
  <svg class="abs spinner" viewBox="0 0 32 32" aria-hidden="true"><path d="M16 3a13 13 0 1 1-12.2 8.5" fill="none" stroke="#fff" stroke-width="2.6" stroke-linecap="round"/></svg>
  <p class="abs tagline" style="top:376px">"Lorem Ipsum is simply dummy text of the printing and typesetting industry. Lorem Ipsum&nbsp; the 1500s..."</p>
  <p class="abs copyright">© 2015 PLUMTIDELANTERNHARBOR.EXAMPLE</p>
  <p class="abs rights">all rights reserved</p>
</section>

<!-- ROW 1 · login -->
<section class="screen row-1 col-2 blue-bg" aria-label="Login screen">
  <div class="brand-mark" style="left:75px;top:33px;width:124px;height:124px">
    <span class="brand-name" style="font-size:19px">Wordnest</span>
  </div>
  <div class="abs field" style="top:181px"><svg><use href="#i-user"/></svg>User name</div>
  <div class="abs field" style="top:230px"><svg><use href="#i-lock"/></svg>Password</div>
  <div class="abs login-btn">Login</div>
  <p class="abs create">Create a Account ?</p>
  <p class="abs tagline" style="top:376px">"Lorem Ipsum is simply dummy text of the printing and typesetting industry. Lorem Ipsum&nbsp; the 1500s..."</p>
  <div class="abs divider"></div>
  <div class="abs social" style="left:35px">chatterly</div>
  <div class="abs social" style="left:117px">chirply</div>
  <div class="abs social" style="left:200px">gleamly</div>
</section>

<!-- ROW 1 · four words -->
<section class="screen row-1 col-3" aria-label="Four words entry screen">
  <div class="abs collage" role="img" aria-label="Faded collage of travel photos behind the content"></div>
  <div class="abs status"><span class="carrier">●●●○○ NOVA <svg width="11" height="9"><use href="#i-wifi"/></svg></span><span class="time">4:21 PM</span><span class="carrier"><svg width="7" height="10"><use href="#i-bt"/></svg>100% <svg width="20" height="10"><use href="#i-battery"/></svg></span></div>
  <div class="abs appbar"><svg><use href="#i-mail"/></svg><span class="title">4 Words</span><svg><use href="#i-gear"/></svg></div>
  <div class="abs avatar" role="img" aria-label="User profile photo" style="left:99px;top:52px;width:76px;height:76px"></div>
  <p class="abs welcome" style="top:134px">Welcome Maren Holt!</p>
  <div class="abs words-box"><span class="word">Apple</span><span class="word">Like</span><span class="word">Ship</span><span class="word">Wonder</span></div>
  <div class="abs btn-blue" style="left:93px;top:228px;width:79px;height:33px">ENTER</div>
  <div class="abs btn-blue" style="left:70px;top:277px;width:126px;height:32px">GENERATE WORDS</div>
  <p class="abs recent-title">Recent</p>
  <p class="abs recent-item" style="top:342px"><span>1. back, class, horse, husband.</span><span>x</span></p>
  <p class="abs recent-item" style="top:358px"><span>2. amount, firm, industry, pupil.</span><span>x</span></p>
  <nav class="abs tabbar"><span class="tab"><svg><use href="#i-four"/></svg>4 WORDS</span><span class="tab"><svg><use href="#i-bubble"/></svg>CHAT ROOM</span><span class="tab"><svg><use href="#i-person"/></svg>PROFILE</span><span class="tab"><svg><use href="#i-info"/></svg>ABOUT</span></nav>
</section>

<!-- ROW 1 · profile -->
<section class="screen row-1 col-4" aria-label="Profile screen">
  <div class="abs cover" role="img" aria-label="Cover collage of travel and friendship photos"></div>
  <div class="abs status light"><span class="carrier">●●●○○ NOVA <svg width="11" height="9"><use href="#i-wifi"/></svg></span><span class="time">4:21 PM</span><span class="carrier"><svg width="7" height="10"><use href="#i-bt"/></svg>100% <svg width="20" height="10"><use href="#i-battery"/></svg></span></div>
  <div class="abs appbar" style="color:#fff"><svg><use href="#i-mail"/></svg><span></span><svg><use href="#i-gear"/></svg></div>
  <div class="abs profile-panel"></div>
  <div class="abs avatar" role="img" aria-label="User profile photo" style="left:98px;top:137px;width:78px;height:78px;z-index:2"></div>
  <div class="abs stat" style="left:14px;top:183px">327<small>Reply</small></div>
  <div class="abs stat" style="left:50px;top:183px">12<small>Friends</small></div>
  <div class="abs stat" style="left:192px;top:183px">435K<small>Points</small></div>
  <div class="abs stat" style="left:239px;top:183px">✎<small>Edit</small></div>
  <p class="abs welcome" style="top:214px">Maren Holt</p>
  <p class="abs" style="left:0;width:273px;top:228px;text-align:center;font-size:7px;color:#555">Videogame, Books, Beauty</p>
  <div class="abs grid" style="left:12px;top:242px;width:248px;grid-template-columns:repeat(3,78px);grid-auto-rows:78px">
    <div class="photo" role="img" aria-label="Couple photo outdoors" style="background:var(--photo-a)"></div>
    <div class="photo" role="img" aria-label="Person jumping by the sea" style="background:var(--photo-b)"></div>
    <div class="photo" role="img" aria-label="Friends laughing outdoors" style="background:var(--photo-e)"></div>
    <div class="photo" role="img" aria-label="Holding hands close-up" style="background:#d8d2cc"></div>
    <div class="photo" role="img" aria-label="Couple in warm light" style="background:var(--photo-f)"></div>
    <div class="photo" role="img" aria-label="Couple portrait" style="background:var(--photo-c)"></div>
    <div class="photo" role="img" aria-label="Travel photo" style="background:#7d6a4f"></div>
    <div class="photo" role="img" aria-label="Sunlit field photo" style="background:var(--photo-d)"></div>
    <div class="photo" role="img" aria-label="Snowy scene photo" style="background:#6e9cc6"></div>
  </div>
  <nav class="abs tabbar"><span class="tab"><svg><use href="#i-four"/></svg>4 WORDS</span><span class="tab"><svg><use href="#i-bubble"/></svg>CHAT ROOM</span><span class="tab"><svg><use href="#i-person"/></svg>PROFILE</span><span class="tab"><svg><use href="#i-info"/></svg>ABOUT</span></nav>
</section>

<!-- ROW 2 · side menu -->
<section class="screen row-2 col-1" aria-label="Side menu">
  <div class="abs drawer-peek"></div>
  <div class="abs" style="left:228px;top:20px;width:45px;height:30px;background:#f6f6f6"></div>
  <svg class="abs" style="left:246px;top:25px;width:22px;height:20px"><use href="#i-mail"/></svg>
  <div class="abs avatar chat-avatar" role="img" aria-label="Contact photo" style="left:234px;top:60px"></div>
  <div class="abs bubble" style="left:233px;top:126px;width:60px;height:30px;font-size:6.6px;color:#777">Lorem</div>
  <div class="abs avatar chat-avatar" role="img" aria-label="Contact photo" style="left:234px;top:190px"></div>
  <div class="abs avatar chat-avatar" role="img" aria-label="Contact photo" style="left:234px;top:297px"></div>
  <div class="abs composer" style="left:228px;width:45px"><span class="plus" style="left:10px">+</span></div>

  <div class="abs drawer"></div>
  <div class="abs status light" style="width:273px"><span class="carrier">●●●○○ NOVA <svg width="11" height="9"><use href="#i-wifi"/></svg></span><span class="time">4:21 PM</span><span class="carrier"><svg width="7" height="10"><use href="#i-bt"/></svg>100% <svg width="20" height="10"><use href="#i-battery"/></svg></span></div>
  <svg class="abs" style="left:18px;top:24px;width:22px;height:22px;color:#fff"><use href="#i-gear"/></svg>
  <div class="abs avatar" role="img" aria-label="User profile photo" style="left:87px;top:47px;width:56px;height:56px"></div>
  <p class="abs welcome" style="top:111px;width:228px;color:#fff;font-weight:400;font-size:10.5px">Welcome Maren Holt!</p>
  <div class="abs menu-item" style="top:127px"><svg><use href="#i-chats"/></svg>Chats<span style="flex:1"></span><span class="badge">2</span><svg style="width:10px;height:14px;margin:0 4px 0 10px"><use href="#i-chev"/></svg></div>
  <div class="abs menu-item" style="top:172px"><svg><use href="#i-aboutc"/></svg>About Wordnest</div>
  <div class="abs menu-item" style="top:210px"><svg><use href="#i-help"/></svg>Help</div>
  <div class="abs menu-item" style="top:249px"><svg><use href="#i-terms"/></svg>Terms &amp; Condition</div>
  <div class="abs menu-item" style="top:288px;border-bottom:0"><svg><use href="#i-power"/></svg>Sign Out</div>
  <div class="abs history-bar">Histry<span class="badge" style="background:#555;margin-left:18px;width:16px;height:16px">2</span><span style="flex:1"></span>Clear</div>
  <div class="abs history-item" style="top:379px"><svg width="22" height="22" style="color:#fff"><use href="#i-chats"/></svg><div style="flex:1"><div class="big">5 mIn</div><div class="sub">Apple, Like, Ship, Wonder.</div></div><span class="badge">3</span></div>
  <div class="abs history-item" style="top:418px"><svg width="22" height="22" style="color:#fff"><use href="#i-chats"/></svg><div><div class="big">7:09 <small style="font-size:8px">Am</small></div><div class="sub">Apple, Like, Ship, Wonder.</div></div></div>
</section>

<!-- ROW 2 · chat -->
<section class="screen row-2 col-2" aria-label="Chat screen">
  <div class="abs chat-bg" role="img" aria-label="Faded travel photo backdrop"></div>
  <div class="abs status"><span class="carrier">●●●○○ NOVA <svg width="11" height="9"><use href="#i-wifi"/></svg></span><span class="time">4:21 PM</span><span class="carrier"><svg width="7" height="10"><use href="#i-bt"/></svg>100% <svg width="20" height="10"><use href="#i-battery"/></svg></span></div>
  <div class="abs appbar"><svg><use href="#i-mail"/></svg><span class="title">Chat</span><svg><use href="#i-gear"/></svg></div>
  <div class="abs avatar chat-avatar" role="img" aria-label="Own profile photo" style="left:6px;top:62px"></div>
  <div class="abs bubble" style="left:52px;top:50px;width:211px;height:50px"><div class="bubble-head"><span>Me.</span><span>19/04/2015. 5:07 PM</span></div><p class="bubble-text">Lorem Ipsum is simply dummy text of the printing and typesetting industry. Lorem Ipsum has been the industry's standard dummy text ever since ?</p></div>
  <div class="abs bubble" style="left:3px;top:124px;width:219px;height:30px"><div class="bubble-head"><span>19/04/2015. 5:09 PM</span><span>Tova_015</span></div><p class="bubble-text">Lorem Ipsum is simply dummy text of the printing and.</p></div>
  <div class="abs avatar chat-avatar" role="img" aria-label="Contact profile photo" style="left:227px;top:124px;background:linear-gradient(180deg,#6fb6d8,#3d7fa6)"></div>
  <div class="abs avatar chat-avatar" role="img" aria-label="Own profile photo" style="left:6px;top:192px"></div>
  <div class="abs bubble" style="left:52px;top:180px;width:211px;height:90px"><div class="bubble-head"><span>Me.</span><span>19/04/2015. 5:11 PM</span></div><p class="bubble-text" style="margin-left:68px">Lorem Ipsum is simply dummy text of the printing and typesetting industry. Lorem Ipsum has been the industry's standard dummy text ever since ?</p></div>
  <div class="abs media" role="img" aria-label="Shared photo thumbnail" style="left:65px;top:201px;width:56px;height:57px;border:2px solid #fff;box-shadow:0 0 0 1px #ccc"></div>
  <svg class="abs" style="left:105px;top:246px;width:12px;height:9px"><use href="#i-cloud"/></svg>
  <div class="abs avatar chat-avatar" role="img" aria-label="Own profile photo" style="left:6px;top:297px"></div>
  <div class="abs bubble" style="left:52px;top:286px;width:211px;height:111px"><div class="bubble-head"><span>Me.</span><span>19/04/2015. 5:11 PM</span></div></div>
  <div class="abs media" role="img" aria-label="Shared photo" style="left:63px;top:304px;width:131px;height:86px"></div>
  <svg class="abs" style="left:175px;top:377px;width:14px;height:10px"><use href="#i-cloud"/></svg>
  <div class="abs composer"><span class="input"></span><span class="plus">+</span><span class="send">Send</span></div>
</section>

<!-- ROW 2 · chat with attach panel -->
<section class="screen row-2 col-3" aria-label="Chat screen with attachment options">
  <div class="abs chat-bg" role="img" aria-label="Faded travel photo backdrop"></div>
  <div class="abs status"><span class="carrier">●●●○○ NOVA <svg width="11" height="9"><use href="#i-wifi"/></svg></span><span class="time">4:21 PM</span><span class="carrier"><svg width="7" height="10"><use href="#i-bt"/></svg>100% <svg width="20" height="10"><use href="#i-battery"/></svg></span></div>
  <div class="abs appbar"><svg><use href="#i-mail"/></svg><span class="title">Chat</span><svg><use href="#i-gear"/></svg></div>
  <div class="abs avatar chat-avatar" role="img" aria-label="Own profile photo" style="left:6px;top:62px"></div>
  <div class="abs bubble" style="left:52px;top:50px;width:211px;height:50px"><div class="bubble-head"><span>Me.</span><span>19/04/2015. 5:07 PM</span></div><p class="bubble-text">Lorem Ipsum is simply dummy text of the printing and typesetting industry. Lorem Ipsum has been the industry's standard dummy text ever since ?</p></div>
  <div class="abs bubble" style="left:3px;top:124px;width:219px;height:30px"><div class="bubble-head"><span>19/04/2015. 5:09 PM</span><span>Tova_015</span></div><p class="bubble-text">Lorem Ipsum is simply dummy text of the printing and.</p></div>
  <div class="abs avatar chat-avatar" role="img" aria-label="Contact profile photo" style="left:227px;top:124px;background:linear-gradient(180deg,#6fb6d8,#3d7fa6)"></div>
  <div class="abs avatar chat-avatar" role="img" aria-label="Own profile photo" style="left:6px;top:192px"></div>
  <div class="abs bubble" style="left:52px;top:180px;width:211px;height:90px"><div class="bubble-head"><span>Me.</span><span>19/04/2015. 5:11 PM</span></div><p class="bubble-text" style="margin-left:68px">Lorem Ipsum is simply dummy text of the printing and typesetting industry. Lorem Ipsum has been the industry's standard dummy text ever since ?</p></div>
  <div class="abs media" role="img" aria-label="Shared photo thumbnail" style="left:65px;top:201px;width:56px;height:57px;border:2px solid #fff;box-shadow:0 0 0 1px #ccc"></div>
  <svg class="abs" style="left:105px;top:246px;width:12px;height:9px"><use href="#i-cloud"/></svg>
  <div class="abs avatar chat-avatar" role="img" aria-label="Own profile photo" style="left:6px;top:297px"></div>
  <div class="abs bubble" style="left:52px;top:286px;width:211px;height:111px"><div class="bubble-head"><span>Me.</span><span>19/04/2015. 5:11 PM</span></div></div>
  <div class="abs media" role="img" aria-label="Shared photo" style="left:63px;top:304px;width:131px;height:86px"></div>
  <div class="abs attach-panel">
    <svg class="abs" style="left:19px;top:8px;width:34px;height:26px;color:#fff"><use href="#i-picture"/></svg>
    <span class="abs" style="left:19px;top:38px;font-size:8.5px;font-weight:500">Picture</span>
    <svg class="abs" style="left:84px;top:6px;width:30px;height:30px;color:#fff"><use href="#i-play"/></svg>
    <span class="abs" style="left:87px;top:38px;font-size:8.5px;font-weight:500">Video</span>
    <svg class="abs" style="left:233px;top:22px;width:20px;height:12px" viewBox="0 0 20 12"><path d="M2 2l8 8 8-8" fill="none" stroke="#fff" stroke-width="2"/></svg>
  </div>
  <div class="abs composer"><span class="input"></span><span class="plus">+</span><span class="send">Send</span></div>
</section>

<!-- ROW 2 · gallery modal -->
<section class="screen row-2 col-4" aria-label="Gallery picker">
  <div class="abs chat-bg" role="img" aria-label="Faded travel photo backdrop"></div>
  <div class="abs status"><span class="carrier">●●●○○ NOVA <svg width="11" height="9"><use href="#i-wifi"/></svg></span><span class="time">4:21 PM</span><span class="carrier"><svg width="7" height="10"><use href="#i-bt"/></svg>100% <svg width="20" height="10"><use href="#i-battery"/></svg></span></div>
  <div class="abs appbar"><svg><use href="#i-mail"/></svg><span class="title">Chat</span><svg><use href="#i-gear"/></svg></div>
  <div class="abs composer"><span class="input"></span><span class="plus">+</span><span class="send">Send</span></div>
  <div class="abs dim"></div>
  <div class="abs modal">
    <div class="modal-head">Gallery<span class="close">×</span></div>
    <div class="grid" style="padding:8px 4px 0 4px;grid-template-columns:repeat(3,76px);grid-auto-rows:76px;gap:6px 6px">
      <div class="photo" role="img" aria-label="Couple photo outdoors" style="background:var(--photo-a)"></div>
      <div class="photo" role="img" aria-label="Person jumping by the sea" style="background:var(--photo-b)"></div>
      <div class="photo" role="img" aria-label="Friends laughing outdoors" style="background:var(--photo-e)"></div>
      <div class="photo" role="img" aria-label="Holding hands close-up" style="background:#d8d2cc"></div>
      <div class="photo" role="img" aria-label="Couple in warm light" style="background:var(--photo-f)"></div>
      <div class="photo" role="img" aria-label="Couple portrait" style="background:var(--photo-c)"></div>
      <div class="photo" role="img" aria-label="Travel photo" style="background:#7d6a4f"></div>
      <div class="photo" role="img" aria-label="Sunlit field photo" style="background:var(--photo-d)"></div>
      <div class="photo" role="img" aria-label="Snowy scene photo" style="background:#6e9cc6"></div>
      <div class="photo" role="img" aria-label="Couple photo outdoors" style="background:var(--photo-a)"></div>
      <div class="photo" role="img" aria-label="Person jumping by the sea" style="background:var(--photo-b)"></div>
      <div class="photo" role="img" aria-label="Friends laughing outdoors" style="background:var(--photo-e)"></div>
    </div>
  </div>
</section>

</body>
</html>
```